Harbor Business Cards

I need a business card designed with the following information.

Company Name: Harbor Wealth Management
Name: BriAnne Dockery
Title: Executive Assistant
Cell: (503) 555-0173
Direct Line: (971) 555-0148
Email: brianne@harborwmx.com
Address: 20537 W. Marlowe PKWY Ste. B
Larkfield, OR 97390

I have attached the logo.
I would like it in navy blue and silver.
Thanks.

```html
<!DOCTYPE html>
<html lang="en">
<head>
<meta charset="utf-8">
<title>Harbor Wealth Management – Business Card</title>
<link rel="stylesheet" href="https://fonts.googleapis.com/css2?family=Lato:ital,wght@0,300;0,400;0,700;1,400&display=swap">
<style>
  :root {
    --navy: #1f2a4a;
    --silver-light: #f1f2f4;
    --silver: #dcdee3;
    --rule: #9aa0ad;
    --ink: #1f2a4a;
    --ink-soft: #4b5368;
    --logo-light: #d6d8de;
    --page: #ececec;
    --label: #333333;
  }
  * { box-sizing: border-box; margin: 0; padding: 0; }
  html, body {
    width: 1200px; height: 796px; overflow: hidden;
    background: var(--page);
    font-family: "Lato", Arial, sans-serif;
  }
  .sheet {
    position: relative; width: 1200px; height: 796px;
    display: flex; justify-content: center; align-items: center; gap: 40px;
  }
  .side { display: flex; flex-direction: column; align-items: center; gap: 22px; }
  .side-label { font-weight: 700; font-size: 32px; letter-spacing: 1px; color: var(--label); }
  .card {
    position: relative; width: 540px; height: 324px; overflow: hidden;
    box-shadow: 0 2px 6px rgba(0,0,0,0.15);
  }

  /* Back */
  .card-back {
    background:
      linear-gradient(135deg, transparent 70%, rgba(255,255,255,0.03) 70%),
      linear-gradient(45deg, rgba(10,14,35,0.25) 0%, transparent 35%),
      var(--navy);
    display: flex; flex-direction: column; align-items: center; justify-content: center; gap: 16px;
  }
  .brand-mark { width: 22px; height: 22px; background: var(--logo-light); }
  .brand-name {
    text-align: center; font-weight: 400; font-size: 14px; line-height: 1.7;
    letter-spacing: 5px; text-transform: uppercase; color: var(--logo-light);
    white-space: nowrap;
  }

  /* Front */
  .card-front {
    background:
      linear-gradient(135deg, rgba(255,255,255,0) 55%, rgba(180,184,194,0.25) 55%, rgba(180,184,194,0) 80%),
      linear-gradient(45deg, rgba(170,175,186,0.35) 0%, rgba(255,255,255,0) 45%),
      linear-gradient(180deg, var(--silver-light), var(--silver));
  }
  .band { position: absolute; left: 0; right: 0; height: 34px; background: var(--navy); }
  .band-top { top: 0; }
  .band-bottom { bottom: 0; }

  .front-brand {
    position: absolute; left: 16px; top: 100px; width: 260px;
    display: flex; flex-direction: column; align-items: center; gap: 16px;
  }
  .front-brand .brand-mark { width: 26px; height: 26px; background: var(--navy); }
  .front-brand .brand-name { color: var(--navy); font-size: 13px; letter-spacing: 4px; }

  .contact { position: absolute; left: 276px; top: 56px; width: 240px; }
  .person { text-align: center; }
  .person-name { font-size: 27px; color: var(--ink); line-height: 1.1; white-space: nowrap; }
  .person-name .first { font-weight: 700; }
  .person-name .last { font-weight: 300; }
  .person-title { font-style: italic; font-size: 12.5px; letter-spacing: 2px; color: var(--ink-soft); margin-top: 4px; }
  .contact-row {
    display: flex; align-items: center; gap: 14px;
    font-size: 12.5px; line-height: 1.3; color: var(--ink);
  }
  .contact-row svg { flex: none; width: 14px; height: 14px; fill: var(--ink); }
  .row-phone { margin-top: 22px; }
  .rule { height: 1px; background: var(--rule); margin: 10px 0 10px 28px; width: 190px; }
</style>
</head>
<body>
<main class="sheet">
  <section class="side">
    <div class="card card-back">
      <div class="brand-mark"></div>
      <div class="brand-name">Harbor<br>Wealth Management</div>
    </div>
    <div class="side-label">BACK</div>
  </section>

  <section class="side">
    <div class="card card-front">
      <div class="band band-top"></div>
      <div class="band band-bottom"></div>

      <div class="front-brand">
        <div class="brand-mark"></div>
        <div class="brand-name">Harbor<br>Wealth Management</div>
      </div>

      <div class="contact">
        <div class="person">
          <div class="person-name"><span class="first">BriAnne</span> <span class="last">Dockery</span></div>
          <div class="person-title">Executive Assistant</div>
        </div>

        <div class="contact-row row-phone">
          <svg viewBox="0 0 16 16" aria-hidden="true"><path d="M2 6c0-2 2-3 6-3s6 1 6 3v1h-3V5.5c-1-.4-5-.4-6 0V7H2zM4 8h8l2 5H2z"/></svg>
          <span>(503) 555-0173<br>(971) 555-0148</span>
        </div>
        <div class="rule"></div>
        <div class="contact-row">
          <svg viewBox="0 0 16 16" aria-hidden="true"><path fill-rule="evenodd" d="M8 1a7 7 0 1 1 0 14A7 7 0 0 1 8 1zm0 1.3c-.6.7-1.1 1.9-1.3 3.2h2.6C9.1 4.2 8.6 3 8 2.3zM5.4 5.5c.2-1.1.5-2.1 1-2.8A5.7 5.7 0 0 0 3 5.5zm-2.9 1.3a5.8 5.8 0 0 0 0 2.4h2.8a14 14 0 0 1 0-2.4zm4 0a12 12 0 0 0 0 2.4h3a12 12 0 0 0 0-2.4zm4.2 0a14 14 0 0 1 0 2.4h2.8a5.8 5.8 0 0 0 0-2.4zM13 5.5a5.7 5.7 0 0 0-3.4-2.8c.5.7.8 1.700 1 2.8zM3 10.5a5.7 5.7 0 0 0 3.4 2.8c-.5-.7-.8-1.7-1-2.8zm3.7 0c.2 1.3.7 2.5 1.3 3.2.6-.7 1.1-1.9 1.3-3.2zm3.9 0c-.2 1.1-.5 2.1-1 2.8A5.7 5.7 0 0 0 13 10.5z"/></svg>
          <span>brianne@harborwmx.com</span>
        </div>
        <div class="rule"></div>
        <div class="contact-row">
          <svg viewBox="0 0 16 16" aria-hidden="true"><path fill-rule="evenodd" d="M8 1a5 5 0 0 1 5 5c0 3.5-5 9-5 9S3 9.5 3 6a5 5 0 0 1 5-5zm0 3a2 2 0 1 0 0 4 2 2 0 0 0 0-4z"/></svg>
          <span>20537 W. Marlowe PKWY Ste.<br>B Larkfield, OR 97390</span>
        </div>
      </div>
    </div>
    <div class="side-label">FRONT</div>
  </section>
</main>
</body>
</html>
```